New iOS App design for Boston Startup

We are looking for a new app design for our iPhone app. The current app's design feels outdated and we like to add lots of new functionality and a new navigation as well. A complete overhaul therefore!
We want you to design 5 screens that will have changed the most. The complete wireframes of these 5 pages are attached in the requirements document.
Once the winning design is selected we will award the winner with the designing all other screens (40-50 screens based on the same design). This will be a separate project worth $1000. The winning designer can get more follow up work if both sides are happy about the cooperation.
We will give feedback as soon as the first screen has been uploaded for review. Final decision will be made only after all 5 screens are finished.
We hope you give it your best!
Note: will only communicate through ArtVantle (no skype),
Updates
Reason: Want to give designers a chance to submit their designs as I understand from some, the deadline is too close.
I have raised the award and introduced a 2nd price as well to make it worth your time. I hope you give it your best shot.
Reason: A few of you have asked for an extension of the deadline as time is running out. I will extend by one day. Tell me if you need more.
Industry/Entity Type
Startup
Requirements
Must have
- At least 1 screen before we can give you feedback.
Nice to have
- multiple options of 1 screen to get to a desirable design

```html
<!DOCTYPE html>
<html lang="en">
<head>
<meta charset="utf-8">
<title>Home Screen – Study App</title>
<link rel="stylesheet" href="https://fonts.googleapis.com/css2?family=Roboto:wght@100;300;400;500;700&display=swap">
<style>
  :root {
    --bg: #b4b9bd;
    --screen: #fbfbfb;
    --line: #dcdcdc;
    --teal: #1aa9d4;
    --teal-dark: #1596bd;
    --text: #5c5c5c;
    --text-soft: #777;
    --red: #e5474b;
    --green: #2fd06a;
    --icon: #6a6a6a;
  }
  * { box-sizing: border-box; margin: 0; padding: 0; }
  html, body { width: 1200px; height: 1000px; overflow: hidden; }
  body {
    background: var(--bg);
    font-family: "Roboto", Arial, sans-serif;
    color: var(--text);
    position: relative;
  }
  .screen {
    position: absolute;
    width: 380px;
    height: 565px;
    background: var(--screen);
    box-shadow: 0 10px 30px rgba(0,0,0,.18);
    display: flex;
    flex-direction: column;
    overflow: hidden;
  }
  .screen--a { left: 20px; top: 228px; }
  .screen--b { left: 412px; top: 194px; }
  .screen--c { left: 804px; top: 160px; }

  /* header */
  .app-header {
    height: 60px; flex: none;
    display: flex; align-items: center; justify-content: center;
    position: relative;
    border-bottom: 1px solid var(--line);
  }
  .menu-icon { position: absolute; left: 22px; top: 21px; width: 24px; height: 19px; }
  .app-title { font-weight: 100; font-size: 31px; color: #555; letter-spacing: .5px; }

  /* user row */
  .user-row {
    height: 66px; flex: none;
    display: flex;
    border-bottom: 1px solid var(--line);
  }
  .greeting { width: 190px; padding: 6px 0 0 22px; border-right: 1px solid var(--line); color: var(--teal); }
  .greeting__hello { font-size: 14px; font-weight: 300; }
  .greeting__name { font-size: 37px; font-weight: 300; line-height: 36px; }
  .score { padding: 7px 0 0 14px; }
  .score__label { font-size: 10px; color: #555; letter-spacing: .3px; }
  .score__row { display: flex; align-items: center; gap: 12px; }
  .score__value { font-size: 38px; font-weight: 300; line-height: 36px; color: #555; }
  .score__delta { font-size: 22px; font-weight: 300; color: #555; margin-top: 8px; }
  .arrow-down { width: 14px; height: 22px; }

  /* stats carousel */
  .stats {
    height: 106px; flex: none;
    margin: 0 14px;
    border-bottom: 1px solid var(--line);
    position: relative;
  }
  .stats__period { text-align: center; color: var(--teal); font-size: 16px; padding-top: 22px; }
  .stats__track {
    position: absolute; left: 22px; right: 26px; top: 48px;
    overflow: hidden;
    display: flex; gap: 0; height: 40px;
    border-right: 2px solid #ccc;
  }
  .stat { flex: none; width: 118px; text-align: center; }
  .stat:first-child { margin-left: -14px; }
  .stat__label { color: var(--teal); font-size: 15px; }
  .stat__value { font-weight: 700; font-size: 19px; color: #555; white-space: nowrap; }
  .stat__up { width: 10px; height: 13px; margin: 0 1px; }
  .chev { position: absolute; top: 58px; width: 12px; height: 20px; }
  .chev--prev { left: 2px; }
  .chev--next { right: 2px; }

  .stats--inline { height: 78px; }
  .stats--inline .stats__track { left: 22px; top: 24px; }
  .stats--inline .chev { top: 36px; }
  .stats--inline .stat--period { width: 62px; margin-left: 0; color: var(--teal); font-size: 18px; padding-top: 9px; text-align: left; }
  .stats--inline .stat:nth-child(2) { margin-left: 0; }

  /* shortcut card */
  .shortcuts {
    flex: none;
    margin: 16px 10px 0 14px;
    height: 60px;
    display: flex;
    background: #fff;
    box-shadow: 1px 3px 6px rgba(0,0,0,.22);
  }
  .shortcut { flex: 1; display: flex; flex-direction: column; align-items: center; justify-content: flex-end; padding-bottom: 7px; font-size: 12.5px; color: #555; }
  .shortcut--active { color: var(--teal); flex: .75; }
  .shortcut--wide { flex: 1.15; }
  .shortcut__icon { width: 36px; height: 32px; margin-bottom: 3px; }
  .shortcut__count { font-size: 26px; font-weight: 300; color: var(--teal); line-height: 28px; margin-bottom: 3px; }

  /* next lesson */
  .up-next { text-align: center; font-size: 20px; font-weight: 300; color: #555; margin-top: 36px; flex: none; }
  .next-lesson {
    flex: none;
    margin: 14px 10px 0 14px;
    height: 44px;
    background: var(--teal);
    color: #fff;
    font-size: 19.5px; font-weight: 300;
    display: flex; align-items: center; justify-content: center;
  }

  /* tab bar */
  .tab-bar {
    margin-top: auto; flex: none;
    height: 62px;
    display: flex;
    border-top: 1px solid var(--line);
    background: #f7f7f7;
  }
  .tab { flex: 1; display: flex; flex-direction: column; align-items: center; justify-content: flex-end; padding-bottom: 7px; font-size: 10.5px; color: #666; }
  .tab__icon { width: 36px; height: 32px; margin-bottom: 3px; }
  .tab--active { border-top: 3px solid var(--teal); margin-top: -1px; }
</style>
</head>
<body>

<svg width="0" height="0" style="position:absolute" aria-hidden="true">
  <defs>
    <symbol id="i-menu" viewBox="0 0 24 19"><rect width="24" height="3" fill="#555"/><rect y="8" width="24" height="3" fill="#555"/><rect y="16" width="24" height="3" fill="#555"/></symbol>
    <symbol id="i-down" viewBox="0 0 14 22"><rect x="4" y="0" width="6" height="12" fill="#e5474b"/><path d="M0 11h14L7 22z" fill="#e5474b"/></symbol>
    <symbol id="i-up" viewBox="0 0 10 13"><path d="M5 0l5 6H7v7H3V6H0z" fill="#2fd06a"/></symbol>
    <symbol id="i-prev" viewBox="0 0 12 20"><path d="M10 2L3 10l7 8" fill="none" stroke="#1aa9d4" stroke-width="3.5"/></symbol>
    <symbol id="i-next" viewBox="0 0 12 20"><path d="M2 2l7 8-7 8" fill="none" stroke="#1aa9d4" stroke-width="3.5"/></symbol>
    <symbol id="i-chart" viewBox="0 0 36 32"><rect x="6" y="12" width="7" height="16" fill="#1aa9d4"/><rect x="14.5" y="3" width="7" height="25" fill="#1aa9d4"/><rect x="23" y="14" width="7" height="14" fill="#1aa9d4"/><rect x="3" y="29" width="30" height="2" fill="#1aa9d4"/></symbol>
    <symbol id="i-doc" viewBox="0 0 36 32"><path d="M8 2h14l5 5v23H8z" fill="#fff" stroke="#666" stroke-width="1.2"/><path d="M11 9h9M11 13h12M11 17h8M11 21h10M11 25h12" stroke="#888" stroke-width="1"/><circle cx="26" cy="15" r="5" fill="#fff" stroke="#666" stroke-width="1.4"/><path d="M29.5 18.5l4 4" stroke="#666" stroke-width="2"/></symbol>
    <symbol id="i-book" viewBox="0 0 36 32"><path d="M3 6q7-3 15 1q8-4 15-1v22q-7-3-15 1q-8-4-15-1z" fill="#fff" stroke="#666" stroke-width="1.3"/><path d="M18 7v22" stroke="#666" stroke-width="1.3"/></symbol>
    <symbol id="i-grid" viewBox="0 0 36 32"><rect x="8" y="3" width="20" height="26" fill="#fff" stroke="#666" stroke-width="1.2"/><path d="M18 3v26M8 16h20" stroke="#666" stroke-width="1.2"/><g font-family="Roboto, Arial, sans-serif" font-size="9" fill="#555" text-anchor="middle"><text x="13" y="13">a</text><text x="23" y="13">b</text><text x="13" y="26">c</text><text x="23" y="26">d</text></g></symbol>
    <symbol id="i-home" viewBox="0 0 36 32"><path d="M18 1L2 16h5v15h8v-9h6v9h8V16h5z" fill="#1aa9d4"/></symbol>
    <symbol id="i-pad" viewBox="0 0 36 32"><path d="M9 9h18c5 0 7 5 7 11s-2 8-4 8-4-4-6-6H12c-2 2-4 6-6 6s-4-2-4-8 2-11 7-11z" fill="#fff" stroke="#666" stroke-width="1.3"/><path d="M8 17h6M11 14v6" stroke="#666" stroke-width="1.4"/><circle cx="25" cy="15" r="1.3" fill="#666"/><circle cx="28" cy="18" r="1.3" fill="#666"/></symbol>
    <symbol id="i-test" viewBox="0 0 36 32"><path d="M8 4h17v26H8z" fill="#fff" stroke="#666" stroke-width="1.2"/><path d="M11 10h9M11 14h11M11 18h8M11 22h10M11 26h11" stroke="#888" stroke-width="1"/><path d="M30 2l3 3-11 11-4 1 1-4z" fill="#fff" stroke="#666" stroke-width="1.2"/></symbol>
  </defs>
</svg>

<!-- Option A: daily stats, centred period -->
<section class="screen screen--a">
  <header class="app-header"><svg class="menu-icon"><use href="#i-menu"/></svg><h1 class="app-title">Home</h1></header>
  <div class="user-row">
    <div class="greeting"><p class="greeting__hello">welcome back,</p><p class="greeting__name">NOAM</p></div>
    <div class="score"><p class="score__label">SCORE</p><div class="score__row"><span class="score__value">650</span><svg class="arrow-down"><use href="#i-down"/></svg><span class="score__delta">-18</span></div></div>
  </div>
  <div class="stats">
    <p class="stats__period">Today</p>
    <svg class="chev chev--prev"><use href="#i-prev"/></svg>
    <div class="stats__track">
      <div class="stat"><p class="stat__label">Completion</p><p class="stat__value">34%<svg class="stat__up"><use href="#i-up"/></svg>+4</p></div>
      <div class="stat"><p class="stat__label">Sessions</p><p class="stat__value">20<svg class="stat__up"><use href="#i-up"/></svg>+3</p></div>
      <div class="stat"><p class="stat__label">Min.</p><p class="stat__value">18<svg class="stat__up"><use href="#i-up"/></svg>+10</p></div>
    </div>
    <svg class="chev chev--next"><use href="#i-next"/></svg>
  </div>
  <nav class="shortcuts">
    <div class="shortcut shortcut--active"><svg class="shortcut__icon"><use href="#i-chart"/></svg>Analytics</div>
    <div class="shortcut shortcut--wide"><svg class="shortcut__icon"><use href="#i-doc"/></svg>Course Overview</div>
    <div class="shortcut"><span class="shortcut__count">33</span>Days until test</div>
  </nav>
  <p class="up-next">Up Next:</p>
  <div class="next-lesson">Lesson 4 - Sentence Correction</div>
  <nav class="tab-bar">
    <div class="tab"><svg class="tab__icon"><use href="#i-book"/></svg>Theory</div>
    <div class="tab"><svg class="tab__icon"><use href="#i-grid"/></svg>Practice</div>
    <div class="tab tab--active"><svg class="tab__icon"><use href="#i-home"/></svg>Home</div>
    <div class="tab"><svg class="tab__icon"><use href="#i-pad"/></svg>Games</div>
    <div class="tab"><svg class="tab__icon"><use href="#i-test"/></svg>Tests</div>
  </nav>
</section>

<!-- Option B: weekly stats -->
<section class="screen screen--b">
  <header class="app-header"><svg class="menu-icon"><use href="#i-menu"/></svg><h1 class="app-title">Home</h1></header>
  <div class="user-row">
    <div class="greeting"><p class="greeting__hello">welcome back,</p><p class="greeting__name">NOAM</p></div>
    <div class="score"><p class="score__label">SCORE</p><div class="score__row"><span class="score__value">650</span><svg class="arrow-down"><use href="#i-down"/></svg><span class="score__delta">-18</span></div></div>
  </div>
  <div class="stats">
    <p class="stats__period">This Week</p>
    <svg class="chev chev--prev"><use href="#i-prev"/></svg>
    <div class="stats__track">
      <div class="stat"><p class="stat__label">Completion</p><p class="stat__value">34%<svg class="stat__up"><use href="#i-up"/></svg>+4</p></div>
      <div class="stat"><p class="stat__label">Sessions</p><p class="stat__value">20<svg class="stat__up"><use href="#i-up"/></svg>+3</p></div>
      <div class="stat"><p class="stat__label">Min.</p><p class="stat__value">18<svg class="stat__up"><use href="#i-up"/></svg>+10</p></div>
    </div>
    <svg class="chev chev--next"><use href="#i-next"/></svg>
  </div>
  <nav class="shortcuts">
    <div class="shortcut shortcut--active"><svg class="shortcut__icon"><use href="#i-chart"/></svg>Analytics</div>
    <div class="shortcut shortcut--wide"><svg class="shortcut__icon"><use href="#i-doc"/></svg>Course Overview</div>
    <div class="shortcut"><span class="shortcut__count">33</span>Days until test</div>
  </nav>
  <p class="up-next">Up Next:</p>
  <div class="next-lesson">Lesson 4 - Sentence Correction</div>
  <nav class="tab-bar">
    <div class="tab"><svg class="tab__icon"><use href="#i-book"/></svg>Theory</div>
    <div class="tab"><svg class="tab__icon"><use href="#i-grid"/></svg>Practice</div>
    <div class="tab tab--active"><svg class="tab__icon"><use href="#i-home"/></svg>Home</div>
    <div class="tab"><svg class="tab__icon"><use href="#i-pad"/></svg>Games</div>
    <div class="tab"><svg class="tab__icon"><use href="#i-test"/></svg>Tests</div>
  </nav>
</section>

<!-- Option C: compact inline stats -->
<section class="screen screen--c">
  <header class="app-header"><svg class="menu-icon"><use href="#i-menu"/></svg><h1 class="app-title">Home</h1></header>
  <div class="user-row">
    <div class="greeting"><p class="greeting__hello">welcome back,</p><p class="greeting__name">NOAM</p></div>
    <div class="score"><p class="score__label">SCORE</p><div class="score__row"><span class="score__value">650</span><svg class="arrow-down"><use href="#i-down"/></svg><span class="score__delta">-18</span></div></div>
  </div>
  <div class="stats stats--inline">
    <svg class="chev chev--prev"><use href="#i-prev"/></svg>
    <div class="stats__track">
      <div class="stat stat--period">Today</div>
      <div class="stat"><p class="stat__label">Completion</p><p class="stat__value">34%<svg class="stat__up"><use href="#i-up"/></svg>+4</p></div>
      <div class="stat"><p class="stat__label">Sessions</p><p class="stat__value">20<svg class="stat__up"><use href="#i-up"/></svg>+3</p></div>
      <div class="stat"><p class="stat__label">Min.</p><p class="stat__value">18<svg class="stat__up"><use href="#i-up"/></svg>+10</p></div>
    </div>
    <svg class="chev chev--next"><use href="#i-next"/></svg>
  </div>
  <nav class="shortcuts">
    <div class="shortcut shortcut--active"><svg class="shortcut__icon"><use href="#i-chart"/></svg>Analytics</div>
    <div class="shortcut shortcut--wide"><svg class="shortcut__icon"><use href="#i-doc"/></svg>Course Overview</div>
    <div class="shortcut"><span class="shortcut__count">33</span>Days until test</div>
  </nav>
  <p class="up-next">Up Next:</p>
  <div class="next-lesson">Lesson 4 - Sentence Correction</div>
  <nav class="tab-bar">
    <div class="tab"><svg class="tab__icon"><use href="#i-book"/></svg>Theory</div>
    <div class="tab"><svg class="tab__icon"><use href="#i-grid"/></svg>Practice</div>
    <div class="tab tab--active"><svg class="tab__icon"><use href="#i-home"/></svg>Home</div>
    <div class="tab"><svg class="tab__icon"><use href="#i-pad"/></svg>Games</div>
    <div class="tab"><svg class="tab__icon"><use href="#i-test"/></svg>Tests</div>
  </nav>
</section>

</body>
</html>
```